習字教室1枚(習字の墨まる®️)そろばん教室1枚(明星のそろばん®️)の2点、野点看板のデザインをそれぞれ1枚もの、合計2枚のデザインをお願いしたいです。ある幼稚園の駐車場に設置するものです。看板の表裏に、それぞれ、明星のそろばん、習字の墨まるの看板が設置されます。(詳細は設置場所および看板の設置場所の写真があります。添付でご覧いただければ幸いです)その駐車場にはすぐ隣に県道が通っていまして、そこから、今回依頼する看板を、車から、駐車場から見た人が’すぐに視覚的に認識できるような野点の看板を作りたいと思っています。
あまりぐちゃぐちゃと情報を詰め込みたくはないと考えています。パッと見て、この順番で認識してもらえるような看板であったらと思っています。
「あっ!そろばん教室があるんだ。」→「明星のそろばん®️ていうんだ」→「そろばん式の暗算力は一生の財産」
「あっ!習字教室があるんだ。」→「習字の墨まる®️って言うんだ」→「きれいな文字は、品格、そして一生の財産」
ロゴ等、設置場所の写真、野立看板の寸法、それぞれのブランドロゴデータは添付してあります。また、サイトをご覧いただいて、よりブランドイメージを膨らませていただけたら幸いです。
習字の墨まるサイト → http://www.sumimaru-shuji.com
明星のそろばんサイト → http://www.meiseisoroban-kyoshitsu.jp
記載項目
①ブランド名(習字の墨まる®️、明星のそろばん®️)、②フリーダイアル、③検索窓に、「習字の墨まる」、「明星のそろばん」と入れたロゴ、、④「大森台市立図書館すぐ」、(この①から④を添付した、習字教室の看板の下の順番通りで。)サイズも添付した以前の習字看板に寸法がふってあります。それで寸法だしはしていただければと思います。すぐに看板屋さんに渡せられる仕様でお渡しいただければ幸いです。

入れていただきたい文言、

習字の方は①「習字教室」②「習字の墨まる®︎」③「きれいな文字は、品格、そして一生の財産」。

そろばんの方は①「そろばん教室」②「明星のそろばん®︎」③「そろばん式の暗算力は一生の財産」

習字、そろばん共に、①の文言は一番大きくしてください。

こちらの趣旨が一番反映されていると感じたところです。

貴重なお時間をいただき、本当にありがとうございました。どれも素晴らしい提案で本当に感動しており、クラフタスの可能性をより感じさせていただきました。今後ともこれに懲りずによろしくお願いいたします。

```html
<!DOCTYPE html>
<html lang="ja">
<head>
<meta charset="utf-8">
<title>野立看板デザイン 習字教室・そろばん教室</title>
<link rel="stylesheet" href="https://fonts.googleapis.com/css2?family=M+PLUS+Rounded+1c:wght@500;800&family=Noto+Sans+JP:wght@400;700;900&display=swap">
<style>
  :root {
    --page: #ffffff;
    --ink: #222222;
    --shodo-green: #1f9a3c;
    --shodo-panel: #ffffff;
    --shodo-accent: #0e6b27;
    --soroban-yellow: #ffd800;
    --soroban-red: #e2231a;
    --soroban-ink: #1a1a1a;
    --search-border: #555555;
    --character-fill: #f3e2b8;
  }
  * { margin: 0; padding: 0; box-sizing: border-box; }
  html, body { width: 684px; height: 1200px; overflow: hidden; background: var(--page); }
  body { font-family: "Noto Sans JP", sans-serif; color: var(--ink); }

  .sheet { width: 684px; height: 1200px; display: flex; flex-direction: column; align-items: center; padding-top: 24px; }
  .board-block { display: flex; flex-direction: column; align-items: center; margin-bottom: 34px; }
  .caption { margin-top: 14px; font-size: 17px; letter-spacing: 0.02em; }

  .signboard {
    width: 320px; height: 480px;
    display: flex; flex-direction: column; align-items: center;
    padding: 16px 18px;
    overflow: hidden;
  }

  /* 習字教室 */
  .signboard--shodo { background: var(--shodo-green); padding-bottom: 10px; }
  .shodo-panel {
    width: 100%; flex: 1; background: var(--shodo-panel);
    display: flex; flex-direction: column; align-items: center; padding: 14px 10px 12px;
  }
  .shodo-character {
    width: 104px; height: 104px; border-radius: 50%; flex-shrink: 0;
    background: radial-gradient(circle, var(--character-fill) 0%, #e0c68a 100%);
    border: 4px solid var(--shodo-green);
  }
  .shodo-title {
    font-family: "Noto Sans JP", sans-serif; font-weight: 900; white-space: nowrap;
    font-size: 56px; line-height: 1.1; color: var(--shodo-accent); margin-top: 8px; letter-spacing: 0.02em;
  }
  .shodo-brand { font-weight: 700; font-size: 22px; line-height: 1.4; color: var(--ink); margin-top: 4px; }
  .shodo-tagline { font-size: 12.5px; font-weight: 700; color: var(--shodo-accent); margin-top: 4px; text-align: center; white-space: nowrap; }

  /* そろばん教室 */
  .signboard--soroban { background: var(--soroban-yellow); border: 6px solid var(--soroban-red); }
  .soroban-title {
    font-family: "M PLUS Rounded 1c", sans-serif; font-weight: 800;
    font-size: 58px; line-height: 1.15; color: var(--soroban-red); text-align: center; margin-top: 10px;
  }
  .soroban-tagline { font-size: 15px; font-weight: 700; color: var(--soroban-ink); margin-top: 14px; text-align: center; }
  .soroban-brand { font-weight: 900; font-size: 44px; line-height: 1.1; color: var(--soroban-ink); text-align: center; margin-top: 12px; }

  /* 共通: 連絡・検索・目印 */
  .freedial { display: flex; align-items: center; gap: 6px; margin-top: 14px; font-weight: 900; font-size: 26px; line-height: 1.3; color: var(--ink); }
  .signboard--shodo .freedial { margin-top: 8px; font-size: 24px; }
  .freedial svg { width: 26px; height: 26px; }
  .search-box {
    display: flex; align-items: center; width: 240px; height: 34px; margin-top: 10px; flex-shrink: 0;
    border: 2px solid var(--search-border); background: #fff;
  }
  .signboard--shodo .search-box { margin-top: 8px; }
  .search-box__text { flex: 1; padding-left: 10px; font-size: 15px; font-weight: 700; }
  .search-box__button { width: 40px; height: 100%; background: var(--search-border); display: flex; align-items: center; justify-content: center; }
  .landmark { margin-top: 10px; font-size: 16px; line-height: 1.3; font-weight: 900; color: #fff; }
  .signboard--shodo .landmark { margin-top: 8px; }
  .signboard--soroban .landmark { color: var(--soroban-red); }
</style>
</head>
<body>
<main class="sheet">

  <section class="board-block">
    <div class="signboard signboard--shodo">
      <div class="shodo-panel">
        <div class="shodo-character" role="img" aria-label="習字教室のマスコットキャラクターのイラスト"></div>
        <h1 class="shodo-title">習字教室</h1>
        <p class="shodo-brand">習字の墨まる<sup>®</sup></p>
        <p class="shodo-tagline">きれいな文字は、品格、そして一生の財産</p>
        <p class="freedial">
          <svg viewBox="0 0 24 24" aria-hidden="true"><path d="M6.6 10.8a15 15 0 0 0 6.6 6.6l2.2-2.2a1 1 0 0 1 1-.25 11 11 0 0 0 3.6.6 1 1 0 0 1 1 1V20a1 1 0 0 1-1 1A17 17 0 0 1 3 4a1 1 0 0 1 1-1h3.5a1 1 0 0 1 1 1 11 11 0 0 0 .6 3.6 1 1 0 0 1-.25 1z" fill="#1f9a3c"/></svg>
          0120-000-111
        </p>
        <div class="search-box">
          <span class="search-box__text">習字の墨まる</span>
          <span class="search-box__button"><svg width="18" height="18" viewBox="0 0 24 24" aria-hidden="true"><circle cx="10" cy="10" r="6" fill="none" stroke="#fff" stroke-width="3"/><line x1="15" y1="15" x2="21" y2="21" stroke="#fff" stroke-width="3"/></svg></span>
        </div>
      </div>
      <p class="landmark">大森台市立図書館すぐ</p>
    </div>
    <p class="caption">丘の上幼稚園駐車場 01（西向き）　2700×1800</p>
  </section>

  <section class="board-block">
    <div class="signboard signboard--soroban">
      <h1 class="soroban-title">そろばん<br>教室</h1>
      <p class="soroban-tagline">そろばん式の暗算力は一生の財産</p>
      <p class="soroban-brand">明星の<br>そろばん<sup>®</sup></p>
      <p class="freedial">
        <svg viewBox="0 0 24 24" aria-hidden="true"><path d="M6.6 10.8a15 15 0 0 0 6.6 6.6l2.2-2.2a1 1 0 0 1 1-.25 11 11 0 0 0 3.6.6 1 1 0 0 1 1 1V20a1 1 0 0 1-1 1A17 17 0 0 1 3 4a1 1 0 0 1 1-1h3.5a1 1 0 0 1 1 1 11 11 0 0 0 .6 3.6 1 1 0 0 1-.25 1z" fill="#e2231a"/></svg>
        0120-000-222
      </p>
      <div class="search-box">
        <span class="search-box__text">明星のそろばん</span>
        <span class="search-box__button"><svg width="18" height="18" viewBox="0 0 24 24" aria-hidden="true"><circle cx="10" cy="10" r="6" fill="none" stroke="#fff" stroke-width="3"/><line x1="15" y1="15" x2="21" y2="21" stroke="#fff" stroke-width="3"/></svg></span>
      </div>
      <p class="landmark">大森台市立図書館すぐ</p>
    </div>
    <p class="caption">丘の上幼稚園駐車場 02（東向き）　2700×1800</p>
  </section>

</main>
</body>
</html>
```